Plakat für Schaufenster
Zielgruppe
Moin Moin,
ich habe einen kleinen Fahrradladen in einem historischen Gebäude. Wir führen ein sehr hochwertiges und ausgesuchtes Programm diverser Hersteller und bieten eine umfassende individuelle Beratung
Aufgabenstellung
Ein Fahrradladen ist einerseits ein Handwerksbetrieb anderseits auch ein Handelsbetrieb. Da ich als Einzelkämpfer in meinem Laden arbeite, habe ich diese beiden Betriebe zeitlich voneinander getrennt. Ich arbeite Vormittags in der Werkstatt und Nachmitttags ist mein Laden für Service und Beratung geöffnet, d.h. meine Laden ist nur Nachmittags von 14-18 und Samstag von 10-13 Uhr geöffnet. Durch diese Regelung kann ich kurze Reparaturzeiten und gute Beratung bieten.
Leider denken nun viele Menschen wenn Sie Vormittags vor verschlossener Tür stehen: "der hat es nicht nötig und arbeitet nur noch halbe Tage!".
Nun möchte ich mit einem Plakat im Fenster meinen "geteilten" Betrieb bzw. meine Arbeitsteilung erklären.
Vielleicht in Form einer analogen Uhr mit entsprechender Teilung !?! Aber auch andere Ideen sind herzlich Willkommen !!

```html
<!DOCTYPE html>
<html lang="de">
<head>
<meta charset="utf-8">
<title>Plakat – Werkstatt und Laden</title>
<link rel="stylesheet" href="https://fonts.googleapis.com/css2?family=Antonio:wght@200;300;400&display=swap">
<style>
  :root {
    --paper: #ece7d7;
    --paper-shade: #ddd7c3;
    --sage: #aeac8d;
    --olive: #6b6a35;
    --ink-grey: #7b7b7b;
    --crank: #8c8291;
    --stem: #c9c5b7;
  }
  html, body {
    margin: 0;
    padding: 0;
    width: 872px;
    height: 1200px;
    overflow: hidden;
    background: var(--paper);
  }
  .poster {
    position: relative;
    width: 872px;
    height: 1200px;
    background: radial-gradient(ellipse at 40% 45%, var(--paper) 0%, var(--paper) 55%, var(--paper-shade) 100%);
    font-family: "Antonio", "Arial Narrow", sans-serif;
    overflow: hidden;
  }
  .bike-parts {
    position: absolute;
    left: 0;
    top: 0;
  }
  .hours-box {
    position: absolute;
    box-sizing: border-box;
  }
  .hours-box__title,
  .hours-box__times {
    margin: 0;
    text-transform: uppercase;
    letter-spacing: 0;
    line-height: 1;
    white-space: nowrap;
  }
  .hours-box--workshop {
    left: 51px;
    top: 31px;
    width: 515px;
    height: 299px;
    border: 2px solid var(--sage);
  }
  .hours-box--workshop .hours-box__title {
    height: 170px;
    padding: 56px 0 0 30px;
    box-sizing: border-box;
    border-bottom: 2px solid var(--sage);
    color: var(--sage);
    font-size: 62px;
    font-weight: 400;
  }
  .hours-box--workshop .hours-box__times {
    padding: 36px 0 0 30px;
    color: var(--ink-grey);
    font-size: 44px;
    font-weight: 300;
  }
  .hours-box--shop {
    left: 278px;
    top: 798px;
    width: 430px;
    height: 390px;
    border: 2px solid var(--olive);
  }
  .hours-box--shop .hours-box__title {
    height: 166px;
    padding: 52px 0 0 28px;
    box-sizing: border-box;
    border-bottom: 2px solid var(--olive);
    color: var(--olive);
    font-size: 64px;
    font-weight: 400;
  }
  .hours-box--shop .hours-box__times {
    padding: 40px 30px 0 0;
    text-align: right;
    color: var(--ink-grey);
    font-size: 44px;
    font-weight: 300;
    line-height: 1.6;
  }
</style>
</head>
<body>
<main class="poster">
  <svg class="bike-parts" width="872" height="1200" viewBox="0 0 872 1200">
    <rect class="bike-parts__stem" x="162" y="188" width="312" height="944" rx="60"
          fill="var(--stem)" opacity="0.45"
          role="img" aria-label="Faint silhouette of a bicycle handlebar and stem"/>
    <rect class="bike-parts__crank" x="28" y="398" width="615" height="304" rx="140"
          fill="var(--crank)" opacity="0.55"
          role="img" aria-label="Bicycle chainring with chain and small sprocket"/>
    <g transform="translate(-12,25)">
      <path class="bike-parts__arc-light" d="M387,672 A197 197 0 1 1 688,429"
            fill="none" stroke="var(--sage)" stroke-width="6"/>
      <path class="bike-parts__arc-dark" d="M692,438 A197 197 0 0 1 514,718"
            fill="none" stroke="var(--olive)" stroke-width="6"/>
    </g>
  </svg>

  <section class="hours-box hours-box--workshop">
    <h2 class="hours-box__title">Handwerksbetrieb</h2>
    <p class="hours-box__times">Mo - Fr // Vormittags</p>
  </section>

  <section class="hours-box hours-box--shop">
    <h2 class="hours-box__title">Handelsbetrieb</h2>
    <p class="hours-box__times">Mo - Fr // 14 - 18 Uhr<br>Sa // 10 - 13 Uhr</p>
  </section>
</main>
</body>
</html>
```